Business Card Design Project for an English Teacher

I need a business card design for my new job.
I'd like to start teaching English as a freelance.
My students will be children, teenager, and adults, who don't like or hesitate to study English and I would like to open a door to the new world for them.

I'd like to put the information below;
[right side]
1. name
2. mail address
3. mobile number
4. website or facebook page

[back]
1.my message: Feel free at asking me anything about my classes

2.lesson list such as:
price: 3150 yen ~

calsses:
kids class( mum& dad can join) ... 30 minutes / 45 minutes
students (over age 13).... 60minutes / 90 minutes
Adult (over age 19) .... 60 minutes / 90 minutes

3. I'll have both Web Lesson and Face to Face Lesson

4. Free trial lesson

Target Market(s)

My students will be children, teenager, and adults, who don't like or hesitate to study English

Industry/Entity Type

Business

Requirements
Must have
• designed both side

```html
<!DOCTYPE html>
<html lang="en">
<head>
<meta charset="utf-8">
<title>English Teacher Business Card</title>
<link rel="stylesheet" href="https://fonts.googleapis.com/css2?family=Cutive&family=Bitter:wght@800&family=Source+Sans+3:wght@400&display=swap">
<style>
  :root {
    --leaf-green: #21d000;
    --lime: #88ff00;
    --paper: #ffffff;
    --card-shadow: rgba(0, 0, 0, 0.55);
  }
  * { margin: 0; padding: 0; box-sizing: border-box; }
  html, body {
    width: 1200px;
    height: 900px;
    overflow: hidden;
    background: var(--paper);
  }
  .canvas {
    position: relative;
    width: 1200px;
    height: 900px;
  }
  .card {
    position: absolute;
    left: 339px;
    width: 525px;
    height: 303px;
    box-shadow: 6px 6px 5px var(--card-shadow);
    overflow: hidden;
  }
  .card--front { top: 126px; background: var(--leaf-green); }
  .card--back {
    top: 472px;
    background: var(--paper);
    border: 1px solid #eeeeee;
    color: var(--leaf-green);
  }

  /* front */
  .apple-art {
    position: absolute;
    left: -40px;
    top: 34px;
    width: 262px;
    height: 238px;
    border-radius: 48% 50% 46% 52% / 50% 50% 50% 50%;
    background: radial-gradient(ellipse at 45% 50%, rgba(136, 255, 0, 0.10) 55%, rgba(136, 255, 0, 0.45) 100%);
  }
  .subject-title {
    position: absolute;
    left: 29px;
    top: 139px;
    font-family: "Source Sans 3", sans-serif;
    font-weight: 400;
    font-size: 46px;
    line-height: 1;
    color: var(--paper);
  }
  .contact {
    position: absolute;
    left: 263px;
    top: 94px;
    list-style: none;
    color: var(--paper);
    font-family: "Source Sans 3", sans-serif;
    font-size: 24px;
    line-height: 29px;
  }
  .contact__name {
    font-family: "Cutive", serif;
    font-size: 22px;
  }

  /* back */
  .message-band {
    position: absolute;
    left: 0;
    top: 29px;
    width: 100%;
    height: 40px;
    background: var(--lime);
    color: var(--paper);
    font-family: "Bitter", serif;
    font-weight: 800;
    font-size: 21px;
    line-height: 40px;
    text-align: center;
    white-space: nowrap;
  }
  .heading {
    font-family: "Bitter", serif;
    font-weight: 800;
    font-size: 17px;
  }
  .price {
    position: absolute;
    top: 84px;
    width: 100%;
    text-align: center;
    font-family: "Source Sans 3", sans-serif;
    font-size: 17px;
  }
  .classes-title {
    position: absolute;
    top: 122px;
    width: 100%;
    text-align: center;
  }
  .class-list {
    position: absolute;
    left: 87px;
    top: 146px;
    list-style: none;
    font-family: "Source Sans 3", sans-serif;
    font-size: 16px;
    line-height: 19.5px;
    white-space: nowrap;
  }
  .class-list__group { display: inline-block; width: 229px; }
  .offer {
    position: absolute;
    width: 100%;
    text-align: center;
    white-space: nowrap;
  }
  .offer--modes { top: 218px; }
  .offer--trial { top: 245px; }
</style>
</head>
<body>
<div class="canvas">

  <section class="card card--front" aria-label="Card front">
    <div class="apple-art" role="img" aria-label="Outline drawing of an apple in lime green"></div>
    <div class="subject-title">English</div>
    <ul class="contact">
      <li class="contact__name">NAME</li>
      <li>Address</li>
      <li>Mobile Number</li>
      <li>Website /Facebook</li>
    </ul>
  </section>

  <section class="card card--back" aria-label="Card back">
    <div class="message-band">Feel free to ask me anything about my classes!</div>
    <p class="price"><span class="heading">PRICE:</span> 3150 yen ~</p>
    <p class="heading classes-title">CLASSES</p>
    <ul class="class-list">
      <li><span class="class-list__group">KIDS&nbsp; ( Parents Welcome ) ............</span>30 - 45 minutes</li>
      <li><span class="class-list__group">STUDENTS ( 13+ years old ) .........</span>60 - 90 minutes</li>
      <li><span class="class-list__group">ADULTS ( 19+ years old ) .............</span>60 -90 minutes</li>
    </ul>
    <p class="heading offer offer--modes">Online &amp; In-Person classes available</p>
    <p class="heading offer offer--trial">FREE Trial Lesson</p>
  </section>

</div>
</body>
</html>
```